IT COMPANYcutting edge tec business card

we are IT company that building any apps.
we need business card in japanese and english
You don’t have to include all information in front one you can attach part of that information to back-side
company name : 株式会社ひかりの丘 (BRIGHTHILL Inc.)
concept : cutting-edge technology
role : 取締役 (director)
name : 呉 炫秀 (Oh Hyeonsuk)
post number : 154-0038
address : 東京都世田谷区西若葉台5-14-8 (5-14-8, Nishiwakabadai, Setagaya Ku, Tokyo To, 154-0038, Japan)
Tel:+81-3-5917-2846
Mobile:+81-80-7253-3169
Email : hoh@brighthill-lab.com
website : www.brighthill-lab.com

we dont have logo so please make it as well
we also looking for designer who can make homapage design.

Contact Information for Business Card

cutting-edge design and modern for IT

Font styles to use
Sans Serif

Colors
34a6d7
33b8a4
6092c4
3377b5
886aae
6b449b
b868aa
a64599

Requirements
Must have
• Simple but designed

```html
<!DOCTYPE html>
<html lang="ja">
<head>
<meta charset="utf-8">
<title>BRIGHTHILL Inc. Business Card</title>
<link href="https://fonts.googleapis.com/css2?family=Noto+Sans+JP:wght@400;500&family=Open+Sans:wght@400;600&display=swap" rel="stylesheet">
<style>
  :root {
    --stage: #2b2b2d;
    --brand-blue: #1f5bb0;
    --brand-blue-deep: #164b9c;
    --brand-blue-light: #2a6cc4;
    --accent-orange: #f28c1b;
    --link-blue: #56aef0;
    --paper: #ffffff;
    --ink-grey: #555a63;
  }
  * { margin: 0; padding: 0; box-sizing: border-box; }
  html, body {
    width: 1200px; height: 900px; overflow: hidden;
    background: var(--stage);
    font-family: "Open Sans", "Noto Sans JP", sans-serif;
  }
  .stage {
    position: relative; width: 1200px; height: 900px;
  }
  .card {
    position: absolute;
    width: 540px; height: 310px;
    border-radius: 26px;
    overflow: hidden;
    box-shadow: 0 18px 40px rgba(0,0,0,0.45);
  }
  /* Front side */
  .card-front {
    left: 40px; top: 295px;
    background: linear-gradient(160deg, var(--brand-blue-light) 0%, var(--brand-blue) 55%, var(--brand-blue-deep) 100%);
  }
  .card-front .wordmark {
    position: absolute; left: 70px; top: 108px;
  }
  .wordmark-jp {
    font-family: "Noto Sans JP", sans-serif;
    color: var(--accent-orange);
    font-size: 30px; font-weight: 400; letter-spacing: 1px;
    line-height: 1.2;
  }
  .card-front .wordmark-en {
    font-family: "Open Sans", sans-serif;
    color: var(--paper);
    font-size: 45px; font-weight: 400;
    line-height: 1.15; letter-spacing: 0.5px;
  }
  /* Back side */
  .card-back {
    left: 620px; top: 295px;
    background: var(--paper);
  }
  .card-back .edge-mark {
    position: absolute; left: 0; top: 108px;
    width: 12px; height: 36px;
    background: var(--brand-blue);
  }
  .person {
    position: absolute; left: 32px; top: 100px;
  }
  .person-name {
    font-family: "Noto Sans JP", "Open Sans", sans-serif;
    color: var(--brand-blue);
    font-size: 19px; font-weight: 400; line-height: 1.25;
  }
  .person-role {
    font-family: "Noto Sans JP", sans-serif;
    color: var(--ink-grey);
    font-size: 12px; line-height: 1.4;
  }
  .card-back .wordmark {
    position: absolute; right: 28px; top: 30px; text-align: left;
  }
  .card-back .wordmark-jp { font-size: 21px; }
  .card-back .wordmark-en {
    font-family: "Open Sans", sans-serif;
    color: var(--brand-blue);
    font-size: 26px; font-weight: 400; line-height: 1.2;
  }
  .band {
    position: absolute; inset: 0;
  }
  .contact-list {
    position: absolute; left: 34px; top: 214px;
    list-style: none;
    color: var(--paper);
    font-size: 13px; line-height: 21px;
  }
  .contact-list li { display: flex; align-items: center; gap: 10px; }
  .contact-list svg { width: 12px; height: 12px; flex: none; }
  .contact-list .domain { color: var(--link-blue); }
  .address {
    position: absolute; right: 26px; top: 206px; width: 250px;
    color: var(--paper);
    font-family: "Noto Sans JP", "Open Sans", sans-serif;
    font-size: 11.5px; line-height: 19px;
  }
</style>
</head>
<body>
<main class="stage">

  <section class="card card-front" aria-label="Card front">
    <div class="wordmark">
      <p class="wordmark-jp">株式会社ひかりの丘</p>
      <p class="wordmark-en">BRIGHTHILL Inc</p>
    </div>
  </section>

  <section class="card card-back" aria-label="Card back">
    <svg class="band" width="540" height="310" viewBox="0 0 540 310" aria-hidden="true">
      <defs>
        <linearGradient id="bandFill" x1="0" y1="0" x2="1" y2="1">
          <stop offset="0" stop-color="#2466bd"/>
          <stop offset="1" stop-color="#164b9c"/>
        </linearGradient>
      </defs>
      <polygon points="0,196 540,134 540,310 0,310" fill="url(#bandFill)"/>
      <line x1="0" y1="196" x2="540" y2="134" stroke="#f28c1b" stroke-width="4"/>
    </svg>

    <span class="edge-mark"></span>

    <div class="person">
      <p class="person-name">呉 炫秀 (OH HYEONSUK)</p>
      <p class="person-role">取締役 (director)</p>
    </div>

    <div class="wordmark">
      <p class="wordmark-jp">株式会社ひかりの丘</p>
      <p class="wordmark-en">BRIGHTHILL Inc.</p>
    </div>

    <ul class="contact-list">
      <li>
        <svg viewBox="0 0 24 24" aria-hidden="true"><path fill="#56aef0" d="M6.6 10.8a15 15 0 0 0 6.6 6.6l2.2-2.2a1 1 0 0 1 1-.25 11.4 11.4 0 0 0 3.6.6 1 1 0 0 1 1 1V20a1 1 0 0 1-1 1A17 17 0 0 1 3 4a1 1 0 0 1 1-1h3.5a1 1 0 0 1 1 1c0 1.25.2 2.45.6 3.6a1 1 0 0 1-.25 1z"/></svg>
        +81-80-7253-3169
      </li>
      <li>
        <svg viewBox="0 0 24 24" aria-hidden="true"><path fill="none" stroke="#56aef0" stroke-width="2.4" d="M3 9c0-3 18-3 18 0v2h-5V9H8v2H3zM5 12h14v8H5z"/></svg>
        +81-3-5917-2846
      </li>
      <li>
        <svg viewBox="0 0 24 24" aria-hidden="true"><rect x="2.5" y="5" width="19" height="14" rx="1.5" fill="none" stroke="#56aef0" stroke-width="2.2"/><path d="M3 6l9 7 9-7" fill="none" stroke="#56aef0" stroke-width="2.2"/></svg>
        hoh@brighthill-lab.com
      </li>
      <li>
        <svg viewBox="0 0 24 24" aria-hidden="true"><circle cx="12" cy="12" r="9.5" fill="none" stroke="#56aef0" stroke-width="2.2"/><path d="M2.5 12h19M12 2.5c3.5 3.5 3.5 15.5 0 19M12 2.5c-3.5 3.5-3.5 15.5 0 19" fill="none" stroke="#56aef0" stroke-width="1.8"/></svg>
        <span>www.<span class="domain">brighthill-lab</span>.com</span>
      </li>
    </ul>

    <p class="address">東京都世田谷区西若葉台 (5-14-8, Nishiwakabadai, Setagaya Ku, Tokyo To, 154-0038, Japan)</p>
  </section>

</main>
</body>
</html>
```